Fahrzeugbeschriftung für Handwerksbetrieb
Zielgruppe
Wir sind ein Handwerksbetrieb der Sanitär- / Heizungsbranche und Bäderbau. Über 20 Jahre am Markt mit ca. 90%
Kunden aus der privaten Wohnungswirtschaft . Anspruchsvolle Privatkunden die Verlässligkeit,
Top Know-how sowie unser hohes Engagement schätze, dürfen wir zu unserem langjährigen
Partnern / Kundenstamm zählen.
Als modernes Handwerksunternehmen erstellen wir innovative Komplettlösungen der Wärme-, Lüftung- und Sanitärtechnik aus einer Hand.
Wir sind auch unter den Aspekten des Umweltschutzes und der Energieeffizienz gefordert.
Aufgabenstellung
Schön wäre wenn der Entwurf eben auch unsere Zuverlässigkeit, das technisches Knowh-how sowie
die Modernität der anspruchsvollen Systemtechniken wiederspiegelt. Gerne auch in Abstrakter Bilder- oder
Formensprache im Hintergrund. Bitte keine klassischen 'Tropfen, Welle, Flamme oder Wasserhahn Symbolik!
Das scheint uns zu weit weg von der Idee einer eher dynamischen, schicken, seriösen und dennoch
zurückhaltender Eleganz der Erkennbarkeit. Auch Großformatige Entwürfe können wir uns vorstellen.
Der Vorschlag darf gerne auch eine Vollflächige Beklebung der verschiedenen KFZ ermöglichen um mit dem Digitaldruck alle Gestaltungsmöglichkeiten und Besonderheiten nutzen zu können.

```html
<!DOCTYPE html>
<html lang="de">
<head>
<meta charset="utf-8">
<title>Olaf Brem – Fahrzeugbeschriftung</title>
<link href="https://fonts.googleapis.com/css2?family=Jost:wght@300;400;500&display=swap" rel="stylesheet">
<style>
  :root {
    --teal-deep: #1d5666;
    --teal: #2c6b7b;
    --teal-light: #8fb4bf;
    --silver: #d9dbdd;
    --silver-light: #eceded;
    --ink: #3a3d40;
    --white: #ffffff;
  }
  * { margin: 0; padding: 0; box-sizing: border-box; }
  html, body {
    width: 1200px;
    height: 600px;
    overflow: hidden;
    background: var(--white);
    font-family: "Jost", sans-serif;
  }
  .wrap-design {
    position: absolute;
    left: 100px;
    top: 110px;
    width: 1020px;
    height: 360px;
    border-radius: 28px;
    overflow: hidden;
  }
  .wrap-graphic {
    position: absolute;
    inset: 0;
    width: 100%;
    height: 100%;
  }
  .brand {
    position: absolute;
    left: 100px;
    top: 48px;
    display: flex;
    align-items: center;
    gap: 18px;
    color: var(--white);
  }
  .brand-mark {
    width: 50px;
    height: 50px;
    border: 2px solid var(--white);
    border-radius: 50%;
  }
  .brand-divider {
    width: 1.5px;
    height: 64px;
    background: var(--white);
  }
  .brand-name {
    font-weight: 500;
    font-size: 26px;
    letter-spacing: 10.5px;
    line-height: 1;
  }
  .brand-services {
    margin-top: 10px;
    font-weight: 300;
    font-size: 19px;
    letter-spacing: 3.4px;
    line-height: 1;
  }
  .contact {
    position: absolute;
    left: 575px;
    top: 222px;
    list-style: none;
    color: var(--ink);
    font-weight: 500;
    font-size: 19px;
    letter-spacing: 0.5px;
  }
  .contact-item {
    display: flex;
    align-items: center;
    gap: 12px;
    height: 24px;
  }
  .contact-item + .contact-item { margin-top: 2px; }
  .contact-icon { width: 16px; height: 16px; flex: none; }
</style>
</head>
<body>
  <section class="wrap-design" aria-label="Fahrzeugbeschriftung Seitenansicht">
    <svg class="wrap-graphic" viewBox="0 0 1020 360" preserveAspectRatio="none" aria-hidden="true">
      <defs>
        <linearGradient id="baseFade" x1="0" y1="0" x2="1" y2="0">
          <stop offset="0" stop-color="#1d5666"/>
          <stop offset="0.3" stop-color="#2c6b7b"/>
          <stop offset="0.5" stop-color="#a9c2c9"/>
          <stop offset="0.62" stop-color="#d9dbdd"/>
          <stop offset="1" stop-color="#eceded"/>
        </linearGradient>
        <linearGradient id="lineFade" x1="0" y1="0" x2="1" y2="0">
          <stop offset="0" stop-color="#ffffff" stop-opacity="0.35"/>
          <stop offset="0.55" stop-color="#ffffff" stop-opacity="0.15"/>
          <stop offset="1" stop-color="#ffffff" stop-opacity="0"/>
        </linearGradient>
        <radialGradient id="glow" cx="0.42" cy="0.75" r="0.45">
          <stop offset="0" stop-color="#cfe0e4" stop-opacity="0.55"/>
          <stop offset="1" stop-color="#cfe0e4" stop-opacity="0"/>
        </radialGradient>
      </defs>
      <rect width="1020" height="360" fill="url(#baseFade)"/>
      <rect width="1020" height="360" fill="url(#glow)"/>
      <g fill="none" stroke="url(#lineFade)" stroke-width="1.2">
        <path d="M0 300 C 220 250, 420 200, 700 190"/>
        <path d="M0 314 C 230 266, 430 218, 700 208"/>
        <path d="M0 328 C 240 282, 440 236, 700 226"/>
        <path d="M0 342 C 250 298, 450 254, 700 244"/>
      </g>
      <rect x="0" y="298" width="1020" height="3" fill="#ffffff" opacity="0.12"/>
    </svg>

    <div class="brand">
      <span class="brand-mark"></span>
      <span class="brand-divider"></span>
      <div class="brand-text">
        <p class="brand-name">OLAF BREM</p>
        <p class="brand-services">SANITÄR . HEIZUNG . BÄDER</p>
      </div>
    </div>

    <ul class="contact">
      <li class="contact-item">
        <svg class="contact-icon" viewBox="0 0 16 16" aria-hidden="true">
          <rect width="16" height="16" fill="#2c6b7b"/>
          <path d="M5 3.5 L6.6 5.6 L5.8 6.8 C6.4 8 7.7 9.4 9.1 10.1 L10.3 9.3 L12.4 10.9 L11.3 12.6 C7.7 12.2 4 8.5 3.5 4.6 Z" fill="none" stroke="#ffffff" stroke-width="1"/>
        </svg>
        <span>02153 708215</span>
      </li>
      <li class="contact-item">
        <svg class="contact-icon" viewBox="0 0 16 16" aria-hidden="true">
          <circle cx="8" cy="8" r="8" fill="#2c6b7b"/>
          <circle cx="8" cy="8" r="5" fill="none" stroke="#ffffff" stroke-width="0.9"/>
          <ellipse cx="8" cy="8" rx="2.2" ry="5" fill="none" stroke="#ffffff" stroke-width="0.9"/>
          <line x1="3" y1="8" x2="13" y2="8" stroke="#ffffff" stroke-width="0.9"/>
        </svg>
        <span>brem-shk.de</span>
      </li>
    </ul>
  </section>
</body>
</html>
```